Now Accepting upcoming Consignment's for our up coming online Farm And Construction Equipment Auction April 14-17th
Consign Now
Commission Rates per item
$1-$500 10%
$501-$7000 8%
$ 7000 and up Flat $ 500 fee per item
Many Items Contact us For Custom Commission Rates
Contact Keith At (555)-214-6038, Keith@pellingbids.com
Cant Get It here we offer trucking

```html
<!DOCTYPE html>
<html lang="en">
<head>
<meta charset="utf-8">
<title>Pelling Auction Service – Consignments</title>
<link rel="stylesheet" href="https://fonts.googleapis.com/css2?family=Bebas+Neue&family=Montserrat:wght@500;600;700&display=swap">
<style>
  :root {
    --green: #0f5120;
    --orange: #f39325;
    --ink: #111111;
    --white: #ffffff;
    --sky-top: #dbe6ee;
    --sky-mid: #eef3f6;
    --grass: #8c8a6a;
  }
  * { box-sizing: border-box; margin: 0; padding: 0; }
  html, body { width: 810px; height: 1200px; overflow: hidden; }
  body { background: var(--green); font-family: "Montserrat", sans-serif; color: var(--ink); }
  .flyer { position: absolute; left: 40px; top: 40px; width: 730px; height: 1119px; background: var(--white); overflow: hidden; }
  .hero-photo {
    position: absolute; left: 0; top: 0; width: 730px; height: 609px;
    background: linear-gradient(180deg, var(--sky-top) 0%, var(--sky-mid) 55%, #e4ebe8 72%, #7fa04a 80%, #6d8a3c 88%, var(--grass) 100%);
  }
  .brand { position: absolute; top: 27px; left: 0; width: 730px; text-align: center; }
  .brand-dot { width: 98px; height: 98px; border-radius: 50%; background: var(--orange); margin: 0 auto; }
  .brand-name { font-family: "Bebas Neue", sans-serif; font-size: 30px; color: var(--orange); line-height: 1; margin-top: 6px; letter-spacing: 0.5px; }
  .headline { position: absolute; top: 165px; left: 0; width: 730px; text-align: center; font-family: "Bebas Neue", sans-serif; font-size: 50px; line-height: 1; color: var(--ink); }
  .event-banner { position: absolute; left: 39px; top: 229px; width: 652px; height: 98px; }
  .event-banner svg { position: absolute; inset: 0; }
  .event-banner .text { position: relative; text-align: center; font-weight: 700; font-size: 29px; line-height: 35px; padding-top: 14px; }
  .event-banner .line-1 { color: var(--white); }
  .event-banner .line-2 { color: var(--orange); }
  .pitch { position: absolute; top: 336px; left: 0; width: 730px; text-align: center; font-size: 23px; font-weight: 500; line-height: 31px; }
  .date-tag { position: absolute; left: 105px; top: 580px; width: 520px; height: 57px; }
  .date-tag svg { position: absolute; inset: 0; }
  .date-tag .text { position: relative; display: flex; justify-content: center; align-items: center; height: 57px; gap: 18px; color: var(--white); font-size: 29px; font-weight: 500; }
  .date-tag .sep { width: 2px; height: 26px; background: var(--white); }
  .rates-title { position: absolute; top: 662px; left: 0; width: 730px; text-align: center; font-size: 29px; font-weight: 700; }
  .rates-table { position: absolute; left: 51px; top: 707px; width: 628px; border-collapse: collapse; font-size: 23px; }
  .rates-table th { background: var(--orange); color: var(--white); font-weight: 600; height: 42px; border: 1px solid var(--orange); }
  .rates-table td { height: 41px; text-align: center; border: 1.5px solid var(--orange); font-weight: 500; width: 50%; }
  .custom-note { position: absolute; top: 928px; left: 0; width: 730px; text-align: center; font-size: 25px; font-weight: 700; margin-top: -24px; }
  .custom-note .accent { color: var(--orange); }
  .consign-btn { position: absolute; left: 215px; top: 940px; width: 300px; height: 54px; background: #000; border-radius: 9px; color: var(--white); font-size: 30px; font-weight: 700; display: flex; align-items: center; justify-content: center; }
  .trucking-note { position: absolute; top: 1006px; left: 0; width: 730px; text-align: center; font-size: 19.5px; font-weight: 500; line-height: 27px; }
  .contact-bar { position: absolute; left: 0; bottom: 0; width: 730px; height: 42px; background: var(--orange); color: var(--white); font-size: 20px; font-weight: 600; }
  .contact-bar span { position: absolute; top: 9px; }
  .contact-bar .name { left: 95px; }
  .contact-bar .phone { left: 204px; }
  .contact-bar .email { left: 378px; }
</style>
</head>
<body>
<main class="flyer">
  <div class="hero-photo" role="img" aria-label="Row of green farm tractors and a blue compact loader parked on grass under a pale spring sky"></div>

  <header class="brand">
    <div class="brand-dot"></div>
    <div class="brand-name">Pelling Auction Service</div>
  </header>

  <h1 class="headline">Now Accepting Upcoming Consignments!</h1>

  <div class="event-banner">
    <svg width="652" height="98" viewBox="0 0 652 98"><polygon points="12,0 652,0 638,98 0,98" fill="var(--green)"/></svg>
    <div class="text">
      <div class="line-1">FARM &amp; CONSTRUCTION EQUIPMENT</div>
      <div class="line-2">AUCTION – APRIL 14-17</div>
    </div>
  </div>

  <p class="pitch">Turn your equipment into cash! Get top<br>exposure and competitive commission rates.</p>

  <div class="date-tag">
    <svg width="520" height="57" viewBox="0 0 520 57"><polygon points="12,0 520,0 508,57 0,57" fill="var(--orange)"/></svg>
    <div class="text"><span>ONLINE AUCTION</span><i class="sep"></i><span>APRIL 14-17</span></div>
  </div>

  <h2 class="rates-title">COMMISSION RATES</h2>
  <table class="rates-table">
    <thead><tr><th>Item Price</th><th>Commission Rate</th></tr></thead>
    <tbody>
      <tr><td>$1-$500</td><td>10%</td></tr>
      <tr><td>$501-$7000</td><td>8%</td></tr>
      <tr><td>$7000 and up</td><td>Flat $ 500 fee per item</td></tr>
    </tbody>
  </table>

  <p class="custom-note">CUSTOM RATES AVAILABLE – <span class="accent">CONTACT US!</span></p>

  <div class="consign-btn">CONSIGN NOW</div>

  <p class="trucking-note">Have more items? Contact us for custom commission rates and<br>trucking options. We make it easy to sell!</p>

  <footer class="contact-bar">
    <span class="name">KEITH</span>
    <span class="phone">(555)-214-6038</span>
    <span class="email">Keith@pellingbids.com</span>
  </footer>
</main>
</body>
</html>
```